New Business Card Design Project

Want a simple but attention grabbing business card. Back Side having mainly our logo and basic info-the front side a typical business card.

Contact Information for Business Card

Hearth & Tile Interiors
218 NW Larkspur Rd. Suite 207
Cedar Hollow, Nebraska 68140

phone- 555.482.7093

website is -htidesigns.com

```html
<!DOCTYPE html>
<html lang="en">
<head>
<meta charset="utf-8">
<title>Hearth &amp; Tile Interiors – Business Card</title>
<link href="https://fonts.googleapis.com/css2?family=Exo+2:wght@700;800&display=swap" rel="stylesheet">
<style>
  :root {
    --brand-blue: #2979ff;
    --card-white: #ffffff;
    --page-bg: #ffffff;
    --shadow: rgba(0, 0, 0, 0.28);
  }
  * { margin: 0; padding: 0; box-sizing: border-box; }
  html, body {
    width: 1200px;
    height: 1000px;
    overflow: hidden;
    background: var(--page-bg);
    font-family: "Exo 2", sans-serif;
    color: var(--brand-blue);
  }
  .canvas {
    position: relative;
    width: 1200px;
    height: 1000px;
  }
  .card {
    position: absolute;
    left: 225px;
    width: 765px;
    height: 437px;
    background: var(--card-white);
    box-shadow: 3px 4px 6px var(--shadow);
    overflow: hidden;
  }
  .card--back { top: 46px; }
  .card--front { top: 529px; }
  .card__band {
    position: absolute;
    left: 0;
    top: 0;
    width: 765px;
    height: 55px;
  }
  .card__band polygon { fill: var(--brand-blue); }
  .card__square {
    position: absolute;
    top: 27px;
    width: 57px;
    height: 55px;
    background: var(--brand-blue);
  }
  .card--back .card__square { left: 681px; }
  .card--front .card__square { left: 27px; }
  .brand-name,
  .brand-sub,
  .website,
  .phone,
  .address {
    position: absolute;
    left: 0;
    width: 100%;
    text-align: center;
    font-weight: 800;
    line-height: 1;
  }
  .brand-name {
    text-transform: uppercase;
    letter-spacing: 1px;
  }
  .brand-sub {
    text-transform: uppercase;
    letter-spacing: 18px;
    text-indent: 18px;
  }
  .card--back .brand-name { top: 239px; font-size: 56px; }
  .card--back .brand-sub { top: 303px; font-size: 20px; }
  .card--front .brand-name { top: 178px; font-size: 48px; }
  .card--front .brand-sub { top: 229px; font-size: 17px; letter-spacing: 16px; text-indent: 16px; }
  .website {
    top: 383px;
    font-size: 24px;
    letter-spacing: 3px;
    text-transform: uppercase;
  }
  .phone {
    top: 290px;
    font-size: 48px;
    letter-spacing: 1px;
  }
  .divider {
    position: absolute;
    left: 27px;
    top: 343px;
    width: 711px;
    height: 3px;
    background: var(--brand-blue);
  }
  .address {
    top: 354px;
    font-style: normal;
    font-size: 23px;
    font-weight: 700;
    line-height: 29px;
  }
</style>
</head>
<body>
<main class="canvas">
  <section class="card card--back" aria-label="Card back">
    <svg class="card__band" viewBox="0 0 765 55" aria-hidden="true">
      <polygon points="0,0 765,0 55,54"/>
    </svg>
    <div class="card__square" aria-hidden="true"></div>
    <h1 class="brand-name">Hearth &amp; Tile</h1>
    <p class="brand-sub">Interiors</p>
    <p class="website">www.htidesigns.com</p>
  </section>

  <section class="card card--front" aria-label="Card front">
    <svg class="card__band" viewBox="0 0 765 55" aria-hidden="true">
      <polygon points="0,0 765,0 710,54"/>
    </svg>
    <div class="card__square" aria-hidden="true"></div>
    <h2 class="brand-name">Hearth &amp; Tile</h2>
    <p class="brand-sub">Interiors</p>
    <p class="phone">555.482.7093</p>
    <div class="divider" aria-hidden="true"></div>
    <address class="address">218 NW Larkspur Rd. Suite 207<br>Cedar Hollow, Nebraska 68140</address>
  </section>
</main>
</body>
</html>
```